Recruitment Site Design

We need a design for the login page, about page, and inner pages of a recruitment site for an oil and gas company. Design should be modern, sleek, professional and colors can be blue, green, white, orange or any other recommended colors.

Please also take into consideration that once the users login, they will need to access a form to fill in their information.

** UPDATE: Kindly provide a design for the inner information page consistent with the outer design. Attached is a picture of the basic structure. ***
Updates

Please provide a design for inner pages as shown in the design brief consistent with the registration page provided. 

Reason: We're extending it to get more inside pages.

Target Market(s)

Professionals looking for a career in the oil and gas industry in the Middle East.

Industry/Entity Type

Oil And Gas

Requirements
Must have
• Sleek design

```html
<!DOCTYPE html>
<html lang="en">
<head>
<meta charset="utf-8">
<title>Strata – Technical &amp; Professional Recruitment</title>
<link href="https://fonts.googleapis.com/css2?family=Ubuntu:wght@400;500&display=swap" rel="stylesheet">
<style>
:root{
  --green-top:#b9d49d;
  --green-mid:#9cc27a;
  --green-deep:#7ea75a;
  --lime:#b3d85a;
  --lime-dark:#8cb630;
  --btn-top:#a9cf3a;
  --btn-bottom:#7da41c;
  --ink:#3f4a2f;
  --ink-green:#4f7a2a;
  --muted:#8a8a8a;
  --list:#777;
  --panel:#e7e7e7;
  --white:#fff;
}
*{box-sizing:border-box;margin:0;padding:0}
html,body{width:1200px;height:1031px;overflow:hidden;background:var(--white);font-family:"Ubuntu",sans-serif}
.page{position:relative;width:1200px;height:1031px}
.abs{position:absolute}
.header-band{left:0;top:0;width:1200px;height:133px;background:linear-gradient(#a9c98a 0 7px,var(--green-top) 7px,#a8cb86 70%,var(--green-deep))}
.brand{left:164px;top:34px;font-size:35px;font-weight:500;color:#4c5a3e;letter-spacing:1px}
.nav{left:580px;top:46px;display:flex;gap:28px;font-size:12px;color:#3b4430;list-style:none}
.hero{left:164px;top:100px;width:872px;height:349px;background:linear-gradient(#a5c88a,#8fba68 70%,var(--green-deep));border-radius:0 0 4px 4px;box-shadow:0 -6px 10px -4px rgba(0,0,0,.45)}
.hero h1{left:31px;top:43px;font-size:24px;font-weight:400;color:var(--white)}
.hero h2{left:31px;top:90px;font-size:17px;font-weight:400;color:var(--white)}
.hero ul{left:27px;top:125px;list-style:none;color:#f3f8ec;font-size:12px}
.hero li{height:28px;padding-left:22px;position:relative}
.hero li::before{content:"";position:absolute;left:2px;top:4px;width:8px;height:8px;border-radius:50%;background:radial-gradient(#dfe9d0,#6e9450)}
.btn{display:flex;align-items:center;justify-content:center;background:linear-gradient(var(--btn-top),var(--btn-bottom));color:#2f3d12;border-radius:3px;box-shadow:inset 0 1px 0 rgba(255,255,255,.4)}
.hero .btn{left:51px;top:275px;width:107px;height:31px;font-size:13px}
.hero-photo{left:426px;top:40px;width:422px;height:285px;border-radius:4px;background:linear-gradient(110deg,#dfe6ec 0%,#9aa6ad 35%,#5d6668 55%,#e4c52a 75%,#f2d22c 100%)}
.tabs{left:164px;top:460px;width:872px;height:49px;background:linear-gradient(#c0e06e,var(--lime) 60%,#a4cb48);border-radius:3px 3px 0 0;font-size:14px;color:#3d4a22}
.tabs span{position:absolute;top:15px}
.body{left:164px;top:509px;width:872px;height:411px;background:var(--panel);border-radius:0 0 4px 4px}
.search{left:20px;top:28px;width:174px;height:25px;background:var(--white);border:1px solid #ccc;border-radius:4px;font-size:11px;color:#4b5a2a;padding:6px 10px}
.search svg{position:absolute;right:6px;top:5px}
.companies{left:23px;top:68px;list-style:none;font-size:11px;color:var(--list)}
.companies li{height:26.25px}
.col-title{font-size:12.5px;color:var(--ink-green);line-height:17px}
.copy{font-size:10.5px;line-height:17px;color:var(--muted);text-align:justify}
.col-btn{width:208px;height:31px;font-size:13px;justify-content:flex-start;padding-left:16px}
.sub-box{left:221px;top:274px;width:635px;height:115px;background:var(--white);border-radius:4px}
.email-input{left:16px;top:40px;width:192px;height:24px;border:1px solid #ccc;background:var(--white)}
.sub-btn{left:121px;top:80px;width:87px;height:24px;font-size:12px;border-radius:3px}
.badge{background:#c9d3dc;border-radius:2px}
.footer{left:0;top:970px;width:1200px;height:61px;background:linear-gradient(#8fb36a 0 2px,var(--green-mid) 2px,#a5c784 96%,#8fb36a);font-size:12px;color:#2e3622}
.social{width:26px;height:26px;border-radius:50%;background:#7f9a64;top:16px}
</style>
</head>
<body>
<div class="page">
  <div class="abs header-band"></div>
  <div class="abs brand">Strata</div>
  <ul class="abs nav">
    <li>Home</li><li>About Us</li><li>Jobs</li><li>Clients</li><li>Find Now</li><li>Location</li><li>Contact Us</li>
  </ul>

  <section class="abs hero">
    <h1 class="abs">Technical &amp; Professional</h1>
    <h2 class="abs">Recruitment Specialists</h2>
    <ul class="abs">
      <li>Lorem ipsum dolor sit amet, consectetur adipiscing elit.</li>
      <li>Sed consectetur sagittis libero, et vehicula nisi tincidunt ultricies.</li>
      <li>In semper nunc at velit dapibus vehicula.</li>
      <li>Pellentesque ultrices urna a mi cursus at congue nisl dapibus.</li>
      <li>Integer et augue id nulla tristique ultrices.</li>
    </ul>
    <div class="abs btn">View More</div>
    <div class="abs hero-photo" role="img" aria-label="Worker holding a yellow hard hat in front of a high-rise under construction with a crane"></div>
  </section>

  <nav class="abs tabs">
    <span style="left:22px">Search Jobs</span>
    <span style="left:221px">JOB SEEKERS</span>
    <span style="left:443px">About the Company</span>
  </nav>

  <main class="abs body">
    <div class="abs search">Key Words
      <svg width="14" height="14" viewBox="0 0 14 14"><circle cx="6" cy="6" r="4.2" fill="none" stroke="#8cb630" stroke-width="2"/><path d="M9 9l4 4" stroke="#8cb630" stroke-width="2.4" stroke-linecap="round"/></svg>
    </div>
    <ul class="abs companies">
      <li>Northgate Tubulars Ltd.</li><li>Continental Wellworks</li><li>Harrow-Kent Drilling Canada</li><li>Prairie Polytechnic</li><li>Solvane Energy Inc.</li>
      <li>Northgate Tubulars Ltd.</li><li>Continental Wellworks</li><li>Harrow-Kent Drilling Canada</li><li>Prairie Polytechnic</li><li>Solvane Energy Inc.</li>
    </ul>

    <h3 class="abs col-title" style="left:221px;top:26px;font-weight:400">Employment opportunities in<br>Oil &amp; Gas</h3>
    <p class="abs copy" style="left:221px;top:66px;width:208px">And web page editors now use Lorem Ipsum as their default model text.</p>
    <div class="abs btn col-btn" style="left:221px;top:119px">Recent Job Openings »</div>
    <div class="abs btn col-btn" style="left:221px;top:159px">Update Your Resume »</div>

    <h3 class="abs col-title" style="left:442px;top:26px;font-weight:400">Find candidates to fill your open positions</h3>
    <p class="abs copy" style="left:443px;top:57px;width:411px">It is a long established fact that a reader will be distracted by the readable content of a page when looking at its layout. The point of using Lorem Ipsum is that it has a more-or-less normal distribution of letters, as opposed to using 'Content here, content here', making it look like readable English.</p>
    <p class="abs copy" style="left:443px;top:186px;width:411px">Many desktop publishing packages and web page editors now use Lorem Ipsum as their default model text, and a search for 'lorem ipsum' will uncover many web sites still in their infancy.</p>

    <h3 class="abs col-title" style="left:221px;top:243px;font-weight:400">Sign up For Newsletter</h3>
    <h3 class="abs col-title" style="left:443px;top:243px;font-weight:400">Recruiters</h3>

    <div class="abs sub-box">
      <p class="abs" style="left:17px;top:13px;font-size:11px;color:var(--muted)">Enter your Email id and Subscribe</p>
      <div class="abs email-input"></div>
      <div class="abs btn sub-btn">Subscribe</div>
      <div class="abs badge" style="left:240px;top:12px;width:70px;height:36px;background:#dfe8cf"></div>
      <div class="abs badge" style="left:330px;top:16px;width:92px;height:30px;background:#cfd9ec"></div>
      <div class="abs badge" style="left:462px;top:16px;width:112px;height:36px;background:#d6e0ee"></div>
      <div class="abs badge" style="left:237px;top:70px;width:73px;height:32px;background:#eee6c2"></div>
      <div class="abs badge" style="left:330px;top:68px;width:40px;height:33px;background:#26386e"></div>
    </div>
  </main>

  <footer class="abs footer">
    <span class="abs" style="left:164px;top:23px">Copyright © 2012. All Rights Reserved</span>
    <span class="abs" style="left:474px;top:23px">Terms &amp; Condition&nbsp;&nbsp;&nbsp;|&nbsp;&nbsp;&nbsp;Privacy Policy</span>
    <span class="abs" style="left:746px;top:22px">Social Media</span>
    <span class="abs social" style="left:828px" aria-label="Social network link"></span>
    <span class="abs social" style="left:863px" aria-label="Social network link"></span>
    <span class="abs social" style="left:900px" aria-label="Social network link"></span>
  </footer>
</div>
</body>
</html>
```